Kestrel Property Management email template

Looking for an email template for communications sent to residents that reads well in most email formats including mobile devices. Similar to the attached email, not quite reclaimed wood but something warm with interesting texture

```html
<!DOCTYPE html>
<html lang="en">
<head>
<meta charset="utf-8">
<title>Kestrel Property Management – Resident Email Template</title>
<link href="https://fonts.googleapis.com/css2?family=Montserrat:wght@400;600;700&display=swap" rel="stylesheet">
<style>
  :root {
    --canvas: #ffffff;
    --paper: #ffffff;
    --ink-navy: #1c2447;
    --ink-blue: #2e4a8c;
    --grey-wood-light: #f4f4f4;
    --grey-wood-dark: #e3e3e3;
    --oak-light: #ede0c8;
    --oak-dark: #dbc7a4;
    --sky-top: #8fb0dc;
    --sky-mid: #b9cbe2;
    --facade-light: #9a9ea6;
    --facade-dark: #3c4150;
  }
  * { box-sizing: border-box; margin: 0; padding: 0; }
  html, body {
    width: 1200px;
    height: 1000px;
    overflow: hidden;
    background: var(--canvas);
    font-family: "Montserrat", sans-serif;
  }
  .canvas {
    position: relative;
    width: 1200px;
    height: 1000px;
  }
  .template {
    position: absolute;
    top: 160px;
    width: 495px;
    height: 705px;
    background: var(--paper);
    box-shadow: 0 6px 24px rgba(0, 0, 0, 0.10);
    overflow: hidden;
  }
  .template--grey { left: 82px; }
  .template--oak { left: 608px; }
  .template__art {
    position: absolute;
    inset: 0;
    width: 495px;
    height: 705px;
  }
  .brand {
    position: absolute;
    top: 33px;
    left: 168px;
    display: flex;
    align-items: center;
    gap: 10px;
    color: var(--ink-navy);
    font-weight: 600;
  }
  .brand__mark {
    width: 26px;
    height: 26px;
    background: var(--ink-blue);
  }
  .brand__name {
    display: flex;
    flex-direction: column;
    line-height: 1;
  }
  .brand__word {
    font-size: 22px;
    letter-spacing: 0.5px;
  }
  .brand__tag {
    font-size: 10px;
    letter-spacing: 1px;
    margin-top: 4px;
  }
  .message {
    position: absolute;
    top: 357px;
    left: 101px;
    width: 310px;
    color: var(--ink-blue);
    font-size: 12px;
    line-height: 15px;
    white-space: nowrap;
  }
  .message p + p { margin-top: 15px; }
  .message strong { font-weight: 700; }
</style>
</head>
<body>
<main class="canvas">

  <article class="template template--grey">
    <svg class="template__art" viewBox="0 0 495 705" aria-hidden="false">
      <defs>
        <linearGradient id="grey-wood" x1="0" y1="0" x2="1" y2="0">
          <stop offset="0" stop-color="var(--grey-wood-light)"/>
          <stop offset="0.5" stop-color="var(--grey-wood-dark)"/>
          <stop offset="1" stop-color="var(--grey-wood-light)"/>
        </linearGradient>
        <linearGradient id="photo-grey" x1="0" y1="0" x2="1" y2="1">
          <stop offset="0" stop-color="var(--sky-top)"/>
          <stop offset="0.35" stop-color="var(--sky-mid)"/>
          <stop offset="0.6" stop-color="var(--facade-light)"/>
          <stop offset="1" stop-color="var(--facade-dark)"/>
        </linearGradient>
      </defs>
      <rect width="495" height="705" fill="url(#grey-wood)" role="img" aria-label="Pale grey whitewashed wood grain texture"/>
      <path d="M0,80 H100 V138 H430 Q495,138 495,200 V400 H0 Z" fill="url(#photo-grey)" role="img" aria-label="Photo of a modern apartment building against a blue sky"/>
      <path d="M0,0 H495 V138 H68 Q0,138 0,85 Z" fill="url(#grey-wood)"/>
      <path d="M0,260 Q0,335 70,335 H420 Q495,335 495,395 V705 Q480,655 430,655 H70 Q0,655 0,595 Z" fill="var(--paper)"/>
    </svg>
    <div class="brand">
      <span class="brand__mark"></span>
      <span class="brand__name">
        <span class="brand__word">KESTREL</span>
        <span class="brand__tag">Property Management</span>
      </span>
    </div>
    <div class="message">
      <p><strong>Lorem ipsum dolor</strong> sit amet, consectetuer adipis-<br>cing elit, sed diam nonummy nibh euismod tinci-<br>dunt ut laoreet dolore magna aliquam erat volut-<br>pat. Ut wisi enim ad minim veniam, quis nostrud<br>exerci tation ullamcorper suscipit lobortis nisl ut<br>aliquip ex ea commodo consequat.</p>
      <p>Duis autem vel eum iriure dolor in hendrerit in<br>vulputate velit esse molestie consequat, vel illum<br>dolore eu feugiat <strong>nulla facilisis at vero</strong> eros et<br>accumsan et iusto odio dignissim qui blandit<br>praesent luptatum zzril delenit augue duis dolore<br>te feugait nulla facilisi.</p>
      <p>Lorem ipsum dolor sit amet, cons ectetuer adipis-<br>cing elit, sed diam nonummy <strong>nibh euismod</strong> tinci-<br>dunt ut laoreet dolore magna aliquam erat volut-<br>pat. Ut wisi enim ad minim veniam, quis nostrud.</p>
    </div>
  </article>

  <article class="template template--oak">
    <svg class="template__art" viewBox="0 0 495 705">
      <defs>
        <linearGradient id="oak-wood" x1="0" y1="0" x2="1" y2="0">
          <stop offset="0" stop-color="var(--oak-light)"/>
          <stop offset="0.5" stop-color="var(--oak-dark)"/>
          <stop offset="1" stop-color="var(--oak-light)"/>
        </linearGradient>
        <linearGradient id="photo-oak" x1="0" y1="0" x2="1" y2="1">
          <stop offset="0" stop-color="var(--sky-top)"/>
          <stop offset="0.35" stop-color="var(--sky-mid)"/>
          <stop offset="0.6" stop-color="var(--facade-light)"/>
          <stop offset="1" stop-color="var(--facade-dark)"/>
        </linearGradient>
      </defs>
      <rect width="495" height="705" fill="url(#oak-wood)" role="img" aria-label="Warm light oak plank texture"/>
      <path d="M0,80 H100 V138 H430 Q495,138 495,200 V400 H0 Z" fill="url(#photo-oak)" role="img" aria-label="Photo of a modern apartment building against a blue sky"/>
      <path d="M0,0 H495 V138 H68 Q0,138 0,85 Z" fill="url(#oak-wood)"/>
      <path d="M0,260 Q0,335 70,335 H420 Q495,335 495,395 V705 Q480,655 430,655 H70 Q0,655 0,595 Z" fill="var(--paper)"/>
    </svg>
    <div class="brand">
      <span class="brand__mark"></span>
      <span class="brand__name">
        <span class="brand__word">KESTREL</span>
        <span class="brand__tag">Property Management</span>
      </span>
    </div>
    <div class="message">
      <p><strong>Lorem ipsum dolor</strong> sit amet, consectetuer adipis-<br>cing elit, sed diam nonummy nibh euismod tinci-<br>dunt ut laoreet dolore magna aliquam erat volut-<br>pat. Ut wisi enim ad minim veniam, quis nostrud<br>exerci tation ullamcorper suscipit lobortis nisl ut<br>aliquip ex ea commodo consequat.</p>
      <p>Duis autem vel eum iriure dolor in hendrerit in<br>vulputate velit esse molestie consequat, vel illum<br>dolore eu feugiat <strong>nulla facilisis at vero</strong> eros et<br>accumsan et iusto odio dignissim qui blandit<br>praesent luptatum zzril delenit augue duis dolore<br>te feugait nulla facilisi.</p>
      <p>Lorem ipsum dolor sit amet, cons ectetuer adipis-<br>cing elit, sed diam nonummy <strong>nibh euismod</strong> tinci-<br>dunt ut laoreet dolore magna aliquam erat volut-<br>pat. Ut wisi enim ad minim veniam, quis nostrud.</p>
    </div>
  </article>

</main>
</body>
</html>
```